KRV Ltd Business Card
Professional Biz Card for Kestrel Ridge Ventures IBC Ltd
KRV Ltd Business Card -
Creative Brief
Professional
Milo Harwick
President & CEO
milo@kestrelridgeventures.biz
www.kestrelridgeventures.biz
Skype ID: mharwick should be added.
www.kestrelridgeventures.biz & perhaps a large version of my logo.

```html
<!DOCTYPE html>
<html lang="en">
<head>
<meta charset="utf-8">
<title>KRV Ltd Business Card</title>
<link rel="stylesheet" href="https://fonts.googleapis.com/css2?family=Open+Sans:wght@400;600;700&display=swap">
<style>
  :root {
    --page: #ffffff;
    --card-light-top: #ffffff;
    --card-light-bottom: #dcdcdc;
    --card-dark-top: #2a2a2a;
    --card-dark-bottom: #000000;
    --ink: #1a1a1a;
    --ink-soft: #444444;
    --mark-light: #8a8a8a;
    --mark-dark: #d6d6d6;
    --tab: #111111;
    --rule: #333333;
    --shadow: rgba(0, 0, 0, 0.28);
  }
  * { box-sizing: border-box; margin: 0; padding: 0; }
  html, body {
    width: 1200px; height: 744px; overflow: hidden;
    background: var(--page);
    font-family: "Open Sans", Arial, sans-serif;
  }
  .canvas { position: relative; width: 1200px; height: 744px; }
  .card {
    position: absolute; width: 570px; height: 336px;
    border-radius: 22px; overflow: hidden;
    box-shadow: 0 3px 8px var(--shadow);
  }
  .card--light { background: linear-gradient(180deg, var(--card-light-top), var(--card-light-bottom)); }
  .card--dark { background: linear-gradient(180deg, var(--card-dark-top), var(--card-dark-bottom)); }
  .card--contact { left: 315px; top: 12px; }
  .card--front-light { left: 14px; top: 394px; }
  .card--front-dark { left: 616px; top: 394px; }

  .brand {
    position: absolute; left: 0; right: 0;
    text-align: center; font-weight: 600; letter-spacing: 6px;
    color: var(--mark-light); line-height: 1;
  }
  .card--contact .brand { top: 52px; font-size: 78px; }
  .card--front-light .brand, .card--front-dark .brand { top: 96px; font-size: 96px; }
  .card--front-dark .brand { color: var(--mark-dark); }

  .tab {
    position: absolute; top: 176px; width: 12px; height: 92px;
    background: var(--tab); border-radius: 6px;
  }
  .tab--left { left: -4px; }
  .tab--right { right: -4px; }

  .person { position: absolute; right: 330px; top: 200px; text-align: right; color: var(--ink); }
  .person__name { font-size: 22px; font-weight: 700; line-height: 1.2; white-space: nowrap; }
  .person__role { font-size: 13px; color: var(--ink-soft); }

  .divider { position: absolute; left: 250px; top: 180px; width: 1px; height: 78px; background: var(--rule); }

  .contact { position: absolute; left: 262px; top: 178px; font-size: 13px; color: var(--ink); border-collapse: collapse; }
  .contact th { text-align: left; font-weight: 700; padding: 0 10px 1px 0; width: 50px; }
  .contact td { padding: 0 0 1px 0; white-space: nowrap; }
  .contact td::before { content: ": "; }

  .web {
    position: absolute; left: 0; right: 0; bottom: 20px;
    text-align: center; font-size: 13px; font-weight: 700; color: var(--ink);
  }
  .card--front-dark .web { color: #e6e6e6; }
</style>
</head>
<body>
<main class="canvas">
  <section class="card card--light card--contact" aria-label="Card back with contact details">
    <span class="tab tab--left"></span>
    <span class="tab tab--right"></span>
    <div class="brand">KRV Ltd</div>
    <div class="person">
      <p class="person__name">Milo Harwick</p>
      <p class="person__role">President &amp; CEO</p>
    </div>
    <span class="divider"></span>
    <table class="contact">
      <tr><th>Cell</th><td>+86 139 2047 5512</td></tr>
      <tr><th>Email</th><td>milo@kestrelridgeventures.biz</td></tr>
      <tr><th>Web</th><td>www.kestrelridgeventures.biz</td></tr>
      <tr><th>Skype</th><td>mharwick</td></tr>
    </table>
  </section>

  <section class="card card--light card--front-light" aria-label="Card front, light">
    <div class="brand">KRV Ltd</div>
    <p class="web">www.kestrelridgeventures.biz</p>
  </section>

  <section class="card card--dark card--front-dark" aria-label="Card front, dark">
    <div class="brand">KRV Ltd</div>
    <p class="web">www.kestrelridgeventures.biz</p>
  </section>
</main>
</body>
</html>
```